Tarjetas de visita para empresa de aluminio

Empresa con mas de 40 años vendiendo perfiles de aluminio.
Somos fábrica y almacén, queremos renovar la tarjeta de presentación de nuestros comerciales dando una imgen innovadora y tecnógica mezclado con la calidez del respeto al medio ambiente.
Añado el logo de la empresa y actual cara trasera de la tarjeta de visita, el logo es el simbolo ML y la marca TORVENIK EXTRUSION, la frase 2extrusion y lacado de aluminio" debe cambiarse por "Diseño, extrusión, lacado, anodizado y mecanizado de precisión de aluminio" o en su defecto incluir todos esos servicios que hacemos o una frase mas pegadiza.

We are an aluminium factory, we produce and stock profiles of aluminium.
we want to renew visit card of our sellers, we are looking for something that show innovation, tecnology and environment respect.
Upload our actual logo and back of visit card, logo ML and brand TORVENIK EXTRUSION must be keept.
Text "Extrusion y lacado de aluminio" must be changed for "Diseño, extrusion, lacado, anodizado y mecanizado de precisión de aluminio" or something like that

```html
<!DOCTYPE html>
<html lang="es">
<head>
<meta charset="UTF-8">
<title>Torvenik Extrusion – Tarjetas de visita</title>
<link rel="stylesheet" href="https://fonts.googleapis.com/css2?family=Montserrat:wght@400;500;600;700&display=swap">
<style>
  :root {
    --backdrop: #151515;
    --card-black: #0d0d0d;
    --card-white: #ffffff;
    --panel: #f7f7f7;
    --ink: #111111;
    --ink-soft: #2a2a2a;
    --silver: #cfcfcf;
    --silver-light: #f2f2f2;
    --stripe-dark: #2b2b2b;
  }
  * { margin: 0; padding: 0; box-sizing: border-box; }
  html, body {
    width: 1200px; height: 901px; overflow: hidden;
    background: var(--backdrop);
    font-family: "Montserrat", sans-serif;
  }
  .canvas { position: relative; width: 1200px; height: 901px; }

  /* Front card */
  .card-front {
    position: absolute; left: 284px; top: 111px;
    width: 536px; height: 346px;
    background: var(--card-black);
  }
  .card-front .mark {
    position: absolute; left: 0; right: 0; top: 112px;
    display: flex; justify-content: center; align-items: center; gap: 12px;
  }
  .mark-dot { width: 26px; height: 26px; border-radius: 50%; background: var(--silver); }
  .card-front .mark-name { color: var(--silver-light); font-size: 46px; font-weight: 700; letter-spacing: 2px; }
  .card-front .wordmark {
    position: absolute; left: 0; right: 0; top: 205px; text-align: center;
    color: var(--silver-light); font-size: 21px; font-weight: 700; letter-spacing: 1.5px;
  }
  .card-front .tagline {
    position: absolute; left: 0; right: 0; top: 233px; text-align: center;
    color: var(--silver); font-size: 8.5px; line-height: 12px; font-weight: 500; letter-spacing: 1.6px;
  }

  /* Back card */
  .card-back {
    position: absolute; left: 403px; top: 433px;
    width: 532px; height: 345px;
    background: var(--card-white);
  }
  .card-back .side-stripe {
    position: absolute; right: 0; top: 0; width: 16px; height: 100%;
    background: linear-gradient(to bottom, var(--stripe-dark) 0%, var(--stripe-dark) 49%, #8a8a8a 50%, #e6e6e6 72%, #9a9a9a 88%, #5a5a5a 100%);
  }
  .card-back .mark {
    position: absolute; left: 50px; top: 62px;
    display: flex; align-items: center; gap: 10px;
  }
  .card-back .mark-name { color: var(--ink); font-size: 40px; font-weight: 700; letter-spacing: 2px; }
  .card-back .wordmark {
    position: absolute; left: 206px; top: 60px;
    color: var(--ink); font-size: 21px; font-weight: 700; letter-spacing: 1px;
  }
  .card-back .tagline {
    position: absolute; left: 206px; top: 87px; width: 290px;
    color: var(--ink-soft); font-size: 8px; line-height: 11px; font-weight: 500; letter-spacing: 1.1px;
  }
  .contact-panel {
    position: absolute; left: 198px; top: 151px; width: 298px; height: 183px;
    background: var(--panel);
  }
  .person-name {
    position: absolute; left: 206px; top: 156px;
    color: var(--ink); font-size: 17px; font-weight: 500; letter-spacing: .3px;
  }
  .person-name strong { font-weight: 700; }
  .person-role {
    position: absolute; left: 206px; top: 181px;
    color: var(--ink); font-size: 11px; font-weight: 600;
  }
  .contact-row {
    position: absolute; left: 206px;
    display: flex; gap: 8px; align-items: flex-start;
    color: var(--ink-soft); font-size: 11px; line-height: 14.6px;
  }
  .contact-row svg { flex: none; width: 14px; height: 14px; margin-top: 1px; }
  .contact-row b { font-weight: 700; color: var(--ink); }
  .row-address { top: 211px; }
  .row-phone { top: 263px; }
  .row-mail { top: 286px; }
  .website {
    position: absolute; left: 42px; top: 286px;
    color: var(--ink); font-size: 13px; font-weight: 700;
  }
</style>
</head>
<body>
<div class="canvas">

  <section class="card-front">
    <div class="mark">
      <span class="mark-dot"></span>
      <span class="mark-name">ML</span>
    </div>
    <div class="wordmark">TORVENIK EXTRUSION</div>
    <div class="tagline">DISEÑO, EXTRUSIÓN, LACADO, ANODIZADO<br>Y MECANIZADO DE PRECISIÓN DE ALUMINIO</div>
  </section>

  <section class="card-back">
    <div class="side-stripe"></div>
    <div class="mark">
      <span class="mark-dot"></span>
      <span class="mark-name">ML</span>
    </div>
    <div class="wordmark">TORVENIK EXTRUSION</div>
    <div class="tagline">DISEÑO, EXTRUSIÓN, LACADO, ANODIZADO<br>Y MECANIZADO DE PRECISIÓN DE ALUMINIO</div>

    <div class="contact-panel"></div>
    <div class="person-name">MARCOS LEDESMA <strong>ORTIZ</strong></div>
    <div class="person-role">Commercial</div>

    <div class="contact-row row-address">
      <svg viewBox="0 0 16 16" aria-hidden="true"><circle cx="8" cy="8" r="7.2" fill="none" stroke="#111" stroke-width="1"/><path d="M8 3.6a2.8 2.8 0 0 0-2.8 2.8C5.2 8.5 8 12 8 12s2.8-3.5 2.8-5.6A2.8 2.8 0 0 0 8 3.6z" fill="none" stroke="#111" stroke-width="1"/><circle cx="8" cy="6.4" r="1" fill="#111"/></svg>
      <span>Pol. Ind. Los Arcos - C/ 4 N° 22<br>41980 SAN TELMO DEL RÍO (Sevilla)<br>Apartado de Correos 305</span>
    </div>
    <div class="contact-row row-phone">
      <svg viewBox="0 0 16 16" aria-hidden="true"><circle cx="8" cy="8" r="7.2" fill="none" stroke="#111" stroke-width="1"/><path d="M5.3 4.3l1.4-.2.8 1.9-.9.8a5 5 0 0 0 2.6 2.6l.8-.9 1.9.8-.2 1.4c-3.5.4-6.8-2.9-6.4-6.4z" fill="none" stroke="#111" stroke-width="1" stroke-linejoin="round"/></svg>
      <span><b>M</b> 600 12 34 56 &nbsp;<b>T</b> 955 00 11 22 &nbsp;<b>F</b> 955 00 11 33</span>
    </div>
    <div class="contact-row row-mail">
      <svg viewBox="0 0 16 16" aria-hidden="true"><circle cx="8" cy="8" r="7.2" fill="none" stroke="#111" stroke-width="1"/><rect x="4.5" y="5.5" width="7" height="5" fill="#111"/><path d="M4.5 5.5L8 8.3l3.5-2.8" fill="none" stroke="#fff" stroke-width=".8"/></svg>
      <span>E-mail: marcosledesma@torvenik.com</span>
    </div>
    <div class="website">www.torvenik.com</div>
  </section>

</div>
</body>
</html>
```